The Marrowvale

We need a APP for our members. this is a Private Bar/Venue. history of the brick building is it was built in1898 and was a gentleman club, oyster house, cigar factory and then law offices before we purchased and are beginning restoration.
the APP must include
1. direct texting to the concierge
2. calendar of events
3. veltrin Lock To open the lock, anyone with a code can approach the door, enable their phone's Bluetooth and press the relevant address from the app.
Read more: http://www.brevortgazette.co.uk/gadgetry/article-5182640/no-more-keys-phone-unlocks-your-front-door-from-anywhere.html#qwx8bRT2mkZp
4. Menus from various restaurants from our surrounding area
5. member name and member number to give the feel that the app is personalized
6. the members account balance
7. ability to pay their bill with credit card or zim tally monthly and automatically.
8. link to quöla with its own icon within the app.
9.the ability to reserve the room
Anything else that may of interest for our members that may be relevant that I may not have mentioned since we are new at this...
35 to 60 years of age
Club

```html
<!DOCTYPE html>
<html lang="en">
<head>
<meta charset="utf-8">
<title>Members</title>
<link rel="stylesheet" href="https://fonts.googleapis.com/css2?family=Montserrat:wght@400;500&display=swap">
<style>
  :root {
    --bar-black: #000000;
    --band-grey: #e9e9e9;
    --page-grey: #f2f2f2;
    --card-white: #ffffff;
    --name-ink: #3a3a3a;
    --phone-ink: #7a7a7a;
    --band-ink: #444444;
    --online-green: #2ea84a;
    --busy-red: #f21b14;
    --fab-cyan: #27c6dc;
    --placeholder-grey: #e4e4e4;
  }
  * { margin: 0; padding: 0; box-sizing: border-box; }
  html, body { width: 675px; height: 1200px; overflow: hidden; }
  body {
    position: relative;
    background: var(--page-grey);
    font-family: "Montserrat", sans-serif;
  }
  .status-bar {
    position: absolute; top: 0; left: 0; width: 675px; height: 32px;
    background: var(--bar-black); color: #fff;
    font-size: 17px; display: flex; align-items: center;
  }
  .status-carrier { position: absolute; left: 6px; display: flex; align-items: center; gap: 4px; }
  .status-time { position: absolute; left: 0; right: 0; text-align: center; font-weight: 500; }
  .status-power { position: absolute; right: 8px; display: flex; align-items: center; gap: 6px; }
  .app-header {
    position: absolute; top: 32px; left: 0; width: 675px; height: 80px;
    background: var(--bar-black); color: #fff;
  }
  .app-title {
    position: absolute; top: 0; left: 0; right: 0; line-height: 68px;
    text-align: center; font-size: 30px; font-weight: 400;
  }
  .menu-icon { position: absolute; left: 30px; top: 22px; }
  .pin-icon { position: absolute; left: 562px; top: 18px; }
  .search-icon { position: absolute; left: 618px; top: 20px; }
  .tagline-band {
    position: absolute; top: 112px; left: 0; width: 675px; height: 64px;
    background: var(--band-grey); color: var(--band-ink);
    font-size: 21px; text-align: center; line-height: 64px;
  }
  .member-list {
    position: absolute; top: 192px; left: 14px; width: 647px;
    display: flex; flex-direction: column; gap: 10px; list-style: none;
  }
  .member-card {
    position: relative; height: 106px; background: var(--card-white);
    box-shadow: 0 1px 3px rgba(0,0,0,0.12);
  }
  .member-avatar {
    position: absolute; left: 18px; top: 13px; width: 80px; height: 80px; border-radius: 50%;
  }
  .member-avatar.placeholder { background: var(--placeholder-grey); border: 2px solid #dadada; overflow: hidden; }
  .member-name {
    position: absolute; left: 125px; top: 18px; font-size: 26px; color: var(--name-ink); letter-spacing: 0.3px; white-space: nowrap;
  }
  .member-phone {
    position: absolute; left: 125px; top: 60px; font-size: 18px; color: var(--phone-ink); font-weight: 500;
  }
  .member-status { position: absolute; left: 598px; top: 37px; width: 30px; height: 30px; }
  .chat-button {
    position: absolute; left: 565px; top: 1091px; width: 86px; height: 86px; border-radius: 50%;
    background: var(--fab-cyan); display: flex; align-items: center; justify-content: center;
  }
</style>
</head>
<body>
  <div class="status-bar">
    <div class="status-carrier">
      <svg width="54" height="10" viewBox="0 0 54 10"><g fill="#fff" stroke="#fff"><circle cx="5" cy="5" r="4"/><circle cx="16" cy="5" r="4"/><circle cx="27" cy="5" r="4"/><circle cx="38" cy="5" r="3.5" fill="none"/><circle cx="49" cy="5" r="3.5" fill="none"/></g></svg>
      <span>VELLO</span>
      <svg width="18" height="14" viewBox="0 0 18 14"><path d="M1 5a12 12 0 0 1 16 0M4 8a8 8 0 0 1 10 0M7 11a3.5 3.5 0 0 1 4 0" stroke="#fff" stroke-width="2" fill="none"/></svg>
    </div>
    <div class="status-time">4:21 PM</div>
    <div class="status-power">
      <svg width="10" height="16" viewBox="0 0 10 16"><path d="M1 4l8 8-4 3V1l4 3-8 8" stroke="#888" stroke-width="1.4" fill="none"/></svg>
      <span>22%</span>
      <svg width="40" height="16" viewBox="0 0 40 16"><rect x="1" y="1" width="34" height="14" rx="3" stroke="#fff" stroke-width="1.5" fill="none"/><rect x="3" y="3" width="7" height="10" fill="#fff"/><rect x="36" y="5" width="2.5" height="6" fill="#fff"/></svg>
    </div>
  </div>

  <header class="app-header">
    <svg class="menu-icon" width="32" height="26" viewBox="0 0 32 26"><g stroke="#fff" stroke-width="3" stroke-linecap="round"><line x1="2" y1="3" x2="30" y2="3"/><line x1="2" y1="13" x2="30" y2="13"/><line x1="2" y1="23" x2="30" y2="23"/></g></svg>
    <h1 class="app-title">Members</h1>
    <svg class="pin-icon" width="28" height="34" viewBox="0 0 28 34"><path d="M14 1C7 1 1.5 6.5 1.5 13.5 1.5 22 14 33 14 33s12.5-11 12.5-19.5C26.5 6.5 21 1 14 1z" fill="#fff"/><circle cx="14" cy="13" r="5" fill="#000"/></svg>
    <svg class="search-icon" width="30" height="30" viewBox="0 0 30 30"><circle cx="12" cy="12" r="9.5" stroke="#fff" stroke-width="3.2" fill="none"/><line x1="19" y1="19" x2="28" y2="28" stroke="#fff" stroke-width="3.6" stroke-linecap="round"/></svg>
  </header>

  <div class="tagline-band">Lorem Ipsum is dummy text of typesetting industry.</div>

  <svg width="0" height="0" style="position:absolute">
    <defs>
      <g id="status-away"><g fill="var(--online-green)"><circle cx="15" cy="2.5" r="1.8"/><circle cx="23.8" cy="6.2" r="1.8"/><circle cx="27.5" cy="15" r="1.8"/><circle cx="23.8" cy="23.8" r="1.8"/><circle cx="15" cy="27.5" r="1.8"/><circle cx="6.2" cy="23.8" r="1.8"/><circle cx="2.5" cy="15" r="1.8"/><circle cx="6.2" cy="6.2" r="1.8"/></g></g>
      <g id="status-dnd-away"><g fill="var(--busy-red)"><circle cx="15" cy="2.5" r="1.8"/><circle cx="23.8" cy="6.2" r="1.8"/><circle cx="27.5" cy="15" r="1.8"/><circle cx="23.8" cy="23.8" r="1.8"/><circle cx="15" cy="27.5" r="1.8"/><circle cx="6.2" cy="23.8" r="1.8"/><circle cx="2.5" cy="15" r="1.8"/><circle cx="6.2" cy="6.2" r="1.8"/></g></g>
      <circle id="status-busy" cx="15" cy="15" r="14" fill="var(--busy-red)"/>
      <circle id="status-online" cx="15" cy="15" r="11.5" fill="none" stroke="var(--online-green)" stroke-width="4.5"/>
      <g id="person-silhouette"><circle cx="38" cy="34" r="15" fill="#d2d2d2"/><path d="M10 80c0-20 12-30 28-30s28 10 28 30z" fill="#d2d2d2"/></g>
    </defs>
  </svg>

  <ul class="member-list">
    <li class="member-card">
      <div class="member-avatar" role="img" aria-label="Member photo" style="background:radial-gradient(circle at 50% 55%,#b58a6c,#5d4a3b 70%)"></div>
      <div class="member-name">Corwin Adley</div>
      <div class="member-phone">+1 987 654 3210</div>
      <svg class="member-status" viewBox="0 0 30 30"><use href="#status-away"/></svg>
    </li>
    <li class="member-card">
      <div class="member-avatar" role="img" aria-label="Member photo" style="background:radial-gradient(circle at 50% 50%,#c9a08a,#4a3a36 70%)"></div>
      <div class="member-name">Tobias Wrenn</div>
      <div class="member-phone">+1 987 654 3210</div>
      <svg class="member-status" viewBox="0 0 30 30"><use href="#status-busy"/></svg>
    </li>
    <li class="member-card">
      <div class="member-avatar" role="img" aria-label="Member photo" style="background:radial-gradient(circle at 50% 55%,#f0c6ac,#b0544a 75%)"></div>
      <div class="member-name">Elsa Marrick</div>
      <div class="member-phone">+1 987 654 3210</div>
      <svg class="member-status" viewBox="0 0 30 30"><use href="#status-online"/></svg>
    </li>
    <li class="member-card">
      <div class="member-avatar" role="img" aria-label="Member photo" style="background:radial-gradient(circle at 55% 45%,#b3805e,#2a211c 70%)"></div>
      <div class="member-name">Halden Rooke</div>
      <div class="member-phone">+1 987 654 3210</div>
      <svg class="member-status" viewBox="0 0 30 30"><use href="#status-online"/></svg>
    </li>
    <li class="member-card">
      <div class="member-avatar" role="img" aria-label="Member photo" style="background:radial-gradient(circle at 50% 52%,#d8a88a,#2b1c16 68%)"></div>
      <div class="member-name">Mira Sol</div>
      <div class="member-phone">+1 987 654 3210</div>
      <svg class="member-status" viewBox="0 0 30 30"><use href="#status-away"/></svg>
    </li>
    <li class="member-card">
      <div class="member-avatar placeholder" role="img" aria-label="Empty member photo"><svg width="76" height="76" viewBox="0 0 76 76"><use href="#person-silhouette"/></svg></div>
      <div class="member-name">Dorian Vaskell</div>
      <div class="member-phone">+1 987 654 3210</div>
      <svg class="member-status" viewBox="0 0 30 30"><use href="#status-dnd-away"/></svg>
    </li>
    <li class="member-card">
      <div class="member-avatar" role="img" aria-label="Member photo" style="background:radial-gradient(circle at 50% 45%,#c49a80,#3c4560 72%)"></div>
      <div class="member-name">Fitzhollis Grane</div>
      <div class="member-phone">+1 987 654 3210</div>
      <svg class="member-status" viewBox="0 0 30 30"><use href="#status-online"/></svg>
    </li>
    <li class="member-card">
      <div class="member-avatar" role="img" aria-label="Member photo" style="background:radial-gradient(circle at 50% 50%,#efc7a8,#7b5a3a 60%,#6f8f4a 85%)"></div>
      <div class="member-name">Ivy Dunn</div>
      <div class="member-phone">+1 987 654 3210</div>
      <svg class="member-status" viewBox="0 0 30 30"><use href="#status-busy"/></svg>
    </li>
    <li class="member-card">
      <div class="member-avatar placeholder" role="img" aria-label="Empty member photo"><svg width="76" height="76" viewBox="0 0 76 76"><use href="#person-silhouette"/></svg></div>
      <div class="member-name">Orrin Pellow</div>
      <div class="member-phone">+1 987 654 3210</div>
      <svg class="member-status" viewBox="0 0 30 30"><use href="#status-online"/></svg>
    </li>
  </ul>

  <div class="chat-button" aria-label="Chat with concierge">
    <svg width="54" height="46" viewBox="0 0 54 46">
      <path d="M24 14 A13 13 0 1 1 44 27" stroke="#fff" stroke-width="2.6" fill="none" stroke-linecap="round"/>
      <path d="M44 27l1-6M44 27l-6-1" stroke="#fff" stroke-width="2.4" stroke-linecap="round"/>
      <ellipse cx="21" cy="28" rx="16" ry="12" fill="#fff"/>
      <path d="M9 36l-3 8 10-5z" fill="#fff"/>
      <g fill="var(--fab-cyan)"><circle cx="14" cy="28" r="2"/><circle cx="21" cy="28" r="2"/><circle cx="28" cy="28" r="2"/></g>
    </svg>
  </div>
</body>
</html>
```